Business Cards for Harbourline Coatings Pty Ltd

Hi every one i need a design for my buisness cards. I Want my logo in it and the name of the company needs to stand out Harbourline Coatings Pty Ltd. I want the background of the buisness cards black and i want the font to stand out in either a white or a silver stylish text. I want the design to be simple but original not to in your face if you know what i mean. I want on the back of the buisness cards to have the services that my buisness offers.
• Interior/Exterior
• Residential/Commercial
• Special effects/Texture Coatings
• Water Damage Repair
• Fully qualified
• Pensioner Discount
• 10 Year guarantee
• Fully Insured
• Obligation free quotes
full internal repaints include a proffesionla cleaning service
I want the services on the back to be layed out in an originall way not just dot points. If possible could my logo take up the whole back ground of the back but the text with the services be kind of like transparent so u cvan still see the logo i dont know if its possible it woiuld just look cool if possible. When i pick a design ill give my contact details to the designer to add to the design at the end. Any questions please just ask! Ill upload my logo.
Conatcs will include office phone: Mobile: E-mail - dale@harbourlinecoatings.com.au, Ill also have a Postal address which is a PO Box and my website is www.harbourlinecoatings.com.au

```html
<!DOCTYPE html>
<html lang="en">
<head>
<meta charset="utf-8">
<title>Harbourline Coatings Pty Ltd – Business Cards</title>
<link href="https://fonts.googleapis.com/css2?family=Arimo:wght@400;700&display=swap" rel="stylesheet">
<style>
  :root {
    --stage: #1c1c1c;
    --card: #0b0b0b;
    --card-edge: #232323;
    --lime: #9acd3c;
    --deep-green: #1f8a3a;
    --silver: #e4e4e4;
    --grey: #8a8a8a;
    --ink: #0a0a0a;
  }
  * { box-sizing: border-box; margin: 0; padding: 0; }
  html, body { width: 1200px; height: 984px; overflow: hidden; }
  body {
    background: var(--stage);
    font-family: "Arimo", Arial, sans-serif;
    position: relative;
  }
  .card {
    position: absolute;
    left: 240px;
    width: 720px;
    height: 440px;
    border-radius: 26px;
    overflow: hidden;
    background: radial-gradient(circle at 30% 40%, #1a1a1a 0%, var(--card) 70%);
    border: 1px solid var(--card-edge);
  }
  .card--back { top: 40px; }
  .card--front { top: 504px; }

  /* Back: services */
  .services {
    position: absolute;
    left: -40px;
    top: 70px;
    width: 560px;
    font-size: 21px;
    line-height: 35px;
    white-space: nowrap;
    color: var(--grey);
  }
  .services__row { display: block; }
  .services .hl { color: var(--lime); font-weight: 700; }
  .services .dot { color: #555; padding: 0 10px; }
  .back-rule {
    position: absolute;
    left: 0; top: 398px;
    width: 320px; height: 4px;
    background: linear-gradient(90deg, var(--lime), transparent);
  }
  .brand-panel {
    position: absolute;
    right: 0; top: 0;
    width: 280px; height: 290px;
    background: var(--lime);
    border-radius: 0 0 0 34px;
    border-left: 6px solid var(--deep-green);
    border-bottom: 6px solid var(--deep-green);
    display: flex;
    align-items: center;
    justify-content: center;
    padding: 24px;
  }
  .brand-panel__name {
    font-weight: 700;
    font-size: 28px;
    line-height: 1.2;
    color: var(--ink);
    text-align: center;
    text-transform: uppercase;
  }

  /* Front */
  .front-band { position: absolute; left: 0; top: 0; width: 720px; height: 150px; }
  .holder {
    position: absolute;
    right: 36px; top: 54px;
    color: var(--ink);
  }
  .holder__name { font-size: 30px; font-weight: 700; }
  .holder__role { font-size: 15px; margin-top: -2px; }
  .brand-mark {
    position: absolute;
    left: 122px; top: 140px;
    width: 92px; height: 92px;
    background: var(--lime);
    border-radius: 8px;
    border: 3px solid var(--deep-green);
  }
  .brand-name {
    position: absolute;
    left: 30px; top: 246px;
    width: 280px;
    text-align: center;
    font-weight: 700;
    font-size: 25px;
    line-height: 1.05;
    color: var(--silver);
    text-transform: uppercase;
  }
  .brand-name__sub { display: block; color: var(--lime); font-size: 19px; margin-top: 4px; }
  .contact {
    position: absolute;
    left: 370px; top: 172px;
    color: var(--silver);
    font-size: 19px;
    line-height: 25px;
  }
  .contact__address { margin-bottom: 10px; }
  .contact__line { display: flex; align-items: center; gap: 12px; }
  .contact__line svg { width: 18px; height: 18px; flex: none; }
  .web {
    position: absolute;
    left: 0; right: 0; top: 378px;
    text-align: center;
    color: var(--silver);
    font-size: 21px;
  }
  .web__rule {
    position: absolute;
    left: 150px; width: 420px; height: 3px;
    top: 362px;
    background: linear-gradient(90deg, transparent, var(--lime), transparent);
  }
  .web__rule--low { top: 412px; height: 2px; background: linear-gradient(90deg, transparent, #555, transparent); }
</style>
</head>
<body>

  <section class="card card--back" aria-label="Back of business card">
    <div class="services">
      <span class="services__row">Interior<span class="dot">•</span><span class="hl">Interior/Exterior</span><span class="dot">•</span>Interior/Exterior</span>
      <span class="services__row">/Commercial<span class="dot">•</span><span class="hl">Residential/Commercial</span><span class="dot">•</span>Special</span>
      <span class="services__row"><span class="hl">Special effects/Texture Coatings</span><span class="dot">•</span>Water</span>
      <span class="services__row">mage Repair<span class="dot">•</span><span class="hl">Water Damage Repair</span><span class="dot">•</span>Fully qualified</span>
      <span class="services__row">ified<span class="dot">•</span><span class="hl">Fully qualified</span><span class="dot">•</span>Pensioner Discount</span>
      <span class="services__row">r Discount<span class="dot">•</span><span class="hl">Pensioner Discount</span><span class="dot">•</span>10 Year</span>
      <span class="services__row">guarantee<span class="dot">•</span><span class="hl">10 Year guarantee</span><span class="dot">•</span>Insured</span>
      <span class="services__row">nsured<span class="dot">•</span><span class="hl">Fully Insured</span><span class="dot">•</span>Obligation free</span>
      <span class="services__row">ion free quotes<span class="dot">•</span><span class="hl">Obligation free quotes</span></span>
    </div>
    <div class="back-rule"></div>
    <div class="brand-panel">
      <span class="brand-panel__name">Harbourline<br>Coatings</span>
    </div>
  </section>

  <section class="card card--front" aria-label="Front of business card">
    <svg class="front-band" viewBox="0 0 720 150" preserveAspectRatio="none" aria-hidden="true">
      <path d="M0 0 L720 0 L720 128 L 300 92 C 220 84, 120 50, 0 38 Z" fill="var(--deep-green)"/>
      <path d="M0 0 L720 0 L720 120 L 300 84 C 220 76, 120 42, 0 30 Z" fill="var(--lime)"/>
    </svg>

    <div class="holder">
      <div class="holder__name">Dale Yourname</div>
      <div class="holder__role">owner</div>
    </div>

    <div class="brand-mark" aria-hidden="true"></div>
    <div class="brand-name">Harbourline Coatings<span class="brand-name__sub">Pty Ltd</span></div>

    <div class="contact">
      <div class="contact__address">Your Address Goes Here<br>City, Country, Zipcode</div>
      <div class="contact__line">
        <svg viewBox="0 0 18 18" aria-hidden="true"><rect x="2" y="4" width="14" height="11" rx="2" fill="var(--lime)"/><rect x="5" y="2" width="8" height="4" rx="1" fill="var(--lime)"/></svg>
        <span>(02) 6100 2847</span>
      </div>
      <div class="contact__line">
        <svg viewBox="0 0 18 18" aria-hidden="true"><rect x="5" y="1" width="8" height="16" rx="2" fill="var(--lime)"/><rect x="6.5" y="3" width="5" height="8" fill="var(--ink)"/></svg>
        <span>0400 318 925</span>
      </div>
      <div class="contact__line">
        <svg viewBox="0 0 18 18" aria-hidden="true"><rect x="1" y="4" width="16" height="11" fill="var(--lime)"/><path d="M1 4 L9 10 L17 4" fill="none" stroke="var(--ink)" stroke-width="1.5"/></svg>
        <span>dale@harbourlinecoatings.com.au</span>
      </div>
    </div>

    <div class="web__rule"></div>
    <div class="web">www.harbourlinecoatings.com.au</div>
    <div class="web__rule web__rule--low"></div>
  </section>

</body>
</html>
```